Maple Hollow Bloom Panels Business card

Looking to have a business card design incorporating my logo for my flower wall business.

Industry/Entity Type

Wedding & event planning

Contact Information for Business Card

My business logo, my name - Lena Whitcombe (owner), my tagline - Let us be your something extra, phone # 401-726-3148, email address - maplehollowbloompanels@mailvane.net, my website - maplehollowbloompanels.net, Instagram handle- @maplehollowbloompanels, FB handle Handle - maplehollowbloompanels

Font styles to use
Other font styles liked:
• Sentaina is the font that is used in my logo

Requirements
Must have
• Would like a double sided business card

```html
<!DOCTYPE html>
<html lang="en">
<head>
<meta charset="utf-8">
<title>Maple Hollow Bloom Panels – Business Card</title>
<link rel="stylesheet" href="https://fonts.googleapis.com/css2?family=Great+Vibes&family=Montserrat:wght@300;400;500&family=Poppins:wght@400;700&display=swap">
<style>
  :root {
    --page: #ffffff;
    --paper: #fbfcfb;
    --leaf-wash: #eef2f0;
    --pink: #e295c1;
    --ink: #2b2b2b;
    --icon: #2f3a30;
    --leaf: #3f6b45;
    --leaf-light: #6f9a72;
    --white: #ffffff;
    --gold: #d9b95c;
  }
  * { box-sizing: border-box; margin: 0; padding: 0; }
  html, body { width: 1200px; height: 2606px; overflow: hidden; background: var(--page); }
  .sheet { position: relative; width: 1200px; height: 2606px; }

  .card {
    position: absolute; top: 847px; width: 520px; height: 912px;
    background: var(--paper); overflow: hidden;
    box-shadow: 0 18px 40px rgba(0,0,0,.18);
  }
  .card--front { left: 50px; }
  .card--back { left: 630px; }

  .paper-texture {
    position: absolute; inset: 0;
    background: linear-gradient(160deg, var(--paper) 0%, var(--leaf-wash) 45%, var(--paper) 100%);
  }

  .pink-panel {
    position: absolute; left: 0; right: 0; bottom: 0;
    background: var(--pink); border-radius: 44px 44px 0 0;
  }
  .card--front .pink-panel { top: 438px; }
  .card--back .pink-panel { top: 426px; }

  .leaf-corner {
    position: absolute; bottom: 0; width: 110px; height: 100px;
    background: radial-gradient(ellipse at center, var(--leaf-light) 0%, var(--leaf) 60%, rgba(63,107,69,0) 72%);
  }
  .leaf-corner--left { left: -10px; }
  .leaf-corner--right { right: -10px; }

  /* Front */
  .emblem {
    position: absolute; left: 50%; top: 372px; transform: translate(-50%, -50%);
    width: 380px; height: 380px; border-radius: 50%;
    background: var(--white); border: 3px solid var(--gold);
    box-shadow: 0 0 0 16px var(--white);
    display: flex; align-items: center; justify-content: center; text-align: center;
  }
  .emblem-name {
    font-family: 'Montserrat', sans-serif; font-weight: 400;
    font-size: 34px; line-height: 1.3; color: var(--ink); letter-spacing: 1px;
  }
  .tagline {
    position: absolute; left: 0; right: 0; top: 652px; text-align: center;
    font-family: 'Montserrat', sans-serif; font-weight: 300;
    font-size: 31px; line-height: 1.25; color: var(--white); letter-spacing: 1px;
  }

  /* Back */
  .wordmark {
    position: absolute; left: 0; right: 0; top: 200px; text-align: center;
    font-family: 'Montserrat', sans-serif; font-weight: 400;
    font-size: 30px; color: var(--ink); letter-spacing: 1px;
  }
  .owner-name {
    position: absolute; left: 84px; top: 455px;
    font-family: 'Great Vibes', cursive; font-size: 68px; color: var(--white);
  }
  .owner-role {
    position: absolute; left: 100px; top: 560px;
    font-family: 'Montserrat', sans-serif; font-weight: 400;
    font-size: 22px; letter-spacing: 6px; color: var(--white);
  }
  .contact-list { position: absolute; left: 100px; top: 616px; list-style: none; }
  .contact-item {
    display: flex; align-items: center; gap: 18px;
    font-family: 'Poppins', sans-serif; font-size: 17px; color: var(--white);
    height: 42px;
  }
  .contact-item--phone { font-size: 31px; font-weight: 700; height: 52px; letter-spacing: .5px; }
  .icon-box {
    width: 30px; height: 30px; border-radius: 6px; background: var(--icon);
    display: flex; align-items: center; justify-content: center; flex: none;
  }
  .icon-box svg { width: 18px; height: 18px; }
</style>
</head>
<body>
<main class="sheet">

  <section class="card card--front" aria-label="Business card front">
    <div class="paper-texture" role="img" aria-label="Faint pale leaf pattern on white paper"></div>
    <div class="pink-panel"></div>
    <div class="emblem"><p class="emblem-name">Maple Hollow<br>Bloom Panels</p></div>
    <p class="tagline">LET US BE YOUR<br>SOMETHING EXTRA</p>
    <div class="leaf-corner leaf-corner--left" role="img" aria-label="Green leaf sprig illustration"></div>
    <div class="leaf-corner leaf-corner--right" role="img" aria-label="Green leaf sprig illustration"></div>
  </section>

  <section class="card card--back" aria-label="Business card back">
    <div class="paper-texture" role="img" aria-label="Faint pale leaf pattern on white paper"></div>
    <p class="wordmark">Maple Hollow Bloom Panels</p>
    <div class="pink-panel"></div>
    <p class="owner-name">Lena Whitcombe</p>
    <p class="owner-role">OWNER</p>
    <ul class="contact-list">
      <li class="contact-item contact-item--phone">
        <span class="icon-box"><svg viewBox="0 0 24 24"><path fill="#fff" d="M6.6 10.8a15.1 15.1 0 0 0 6.6 6.6l2.2-2.2a1 1 0 0 1 1-.25 11.4 11.4 0 0 0 3.6.57 1 1 0 0 1 1 1V20a1 1 0 0 1-1 1A17 17 0 0 1 3 4a1 1 0 0 1 1-1h3.5a1 1 0 0 1 1 1c0 1.25.2 2.45.57 3.57a1 1 0 0 1-.25 1z"/></svg></span>
        401-726-3148
      </li>
      <li class="contact-item">
        <span class="icon-box"><svg viewBox="0 0 24 24"><rect x="3" y="6" width="18" height="12" rx="1.5" fill="none" stroke="#fff" stroke-width="2"/><path d="M3.5 7l8.5 6 8.5-6" fill="none" stroke="#fff" stroke-width="2"/></svg></span>
        maplehollowbloompanels@mailvane.net
      </li>
      <li class="contact-item">
        <span class="icon-box"><svg viewBox="0 0 24 24"><circle cx="12" cy="12" r="9" fill="none" stroke="#fff" stroke-width="2"/><ellipse cx="12" cy="12" rx="4" ry="9" fill="none" stroke="#fff" stroke-width="1.6"/><path d="M3 12h18" stroke="#fff" stroke-width="1.6"/></svg></span>
        maplehollowbloompanels.net
      </li>
      <li class="contact-item">
        <span class="icon-box"></span>
        @maplehollowbloompanels
      </li>
      <li class="contact-item">
        <span class="icon-box"></span>
        maplehollowbloompanels
      </li>
    </ul>
    <div class="leaf-corner leaf-corner--left" role="img" aria-label="Green leaf sprig illustration"></div>
    <div class="leaf-corner leaf-corner--right" role="img" aria-label="Green leaf sprig illustration"></div>
  </section>

</main>
</body>
</html>
```